Book Cover " FROM GRAVEL TO AMBER"

Looking for a book cover for a novel from Gravel to Amber.
Amber is the characters developed name. The book describes his rough up bringing and how he obtains his greatness and his given name Amber.

```html
<!DOCTYPE html>
<html lang="en">
<head>
<meta charset="utf-8">
<title>From Gravel to Amber — Book Cover</title>
<link rel="stylesheet" href="https://fonts.googleapis.com/css2?family=Permanent+Marker&family=Cinzel:wght@400;500&display=swap">
<style>
  :root {
    --paper: #ffffff;
    --title-red: #8c2a38;
    --subtitle-red: #6e2832;
    --author-white: #f7efe9;
    --feather-deep: #2b0f22;
    --feather-plum: #5a1f46;
    --feather-magenta: #93345e;
    --feather-amber: #c9683a;
    --feather-ember: #e08a4a;
  }
  html, body {
    margin: 0;
    padding: 0;
    width: 800px;
    height: 1200px;
    overflow: hidden;
    background: var(--paper);
  }
  .cover {
    position: relative;
    width: 800px;
    height: 1200px;
    background: var(--paper);
    overflow: hidden;
  }
  .cover-art {
    position: absolute;
    left: 0;
    top: 0;
    width: 800px;
    height: 1200px;
  }
  .title-block {
    position: absolute;
    top: 215px;
    left: 0;
    width: 100%;
    text-align: center;
  }
  .title-main {
    margin: 0;
    font-family: "Permanent Marker", cursive;
    font-weight: 400;
    font-size: 82px;
    line-height: 1;
    letter-spacing: 0.02em;
    color: var(--title-red);
  }
  .title-sub {
    margin: 14px 0 0;
    font-family: "Cinzel", serif;
    font-weight: 500;
    font-size: 46px;
    line-height: 1;
    letter-spacing: 0.32em;
    padding-left: 0.32em;
    color: var(--subtitle-red);
  }
  .author-name {
    position: absolute;
    bottom: 62px;
    left: 0;
    width: 100%;
    margin: 0;
    text-align: center;
    font-family: "Cinzel", serif;
    font-weight: 400;
    font-size: 42px;
    letter-spacing: 0.2em;
    padding-left: 0.2em;
    color: var(--author-white);
  }
</style>
</head>
<body>
  <main class="cover">
    <svg class="cover-art" viewBox="0 0 800 1200" role="img" aria-label="Close-up of layered feathers in plum, magenta and amber tones, revealed beneath a rough white brush stroke">
      <defs>
        <linearGradient id="feather-base" x1="0" y1="0" x2="1" y2="1">
          <stop offset="0" stop-color="var(--feather-amber)"/>
          <stop offset="0.35" stop-color="var(--feather-magenta)"/>
          <stop offset="0.7" stop-color="var(--feather-plum)"/>
          <stop offset="1" stop-color="var(--feather-deep)"/>
        </linearGradient>
        <radialGradient id="feather-glow" cx="0.3" cy="0.35" r="0.6">
          <stop offset="0" stop-color="var(--feather-ember)" stop-opacity="0.75"/>
          <stop offset="1" stop-color="var(--feather-ember)" stop-opacity="0"/>
        </radialGradient>
        <radialGradient id="feather-shade" cx="0.75" cy="0.85" r="0.6">
          <stop offset="0" stop-color="var(--feather-deep)" stop-opacity="0.7"/>
          <stop offset="1" stop-color="var(--feather-deep)" stop-opacity="0"/>
        </radialGradient>
        <clipPath id="brush-edge">
          <path d="M0 520 L40 505 L70 515 L110 492 L150 508 L190 488 L230 500 L270 478 L320 495 L360 472 L410 488 L450 465 L500 482 L540 460 L590 476 L630 455 L680 470 L720 450 L760 466 L800 448 L800 1200 L0 1200 Z"/>
        </clipPath>
      </defs>
      <g clip-path="url(#brush-edge)">
        <rect x="0" y="440" width="800" height="760" fill="url(#feather-base)"/>
        <rect x="0" y="440" width="800" height="760" fill="url(#feather-glow)"/>
        <rect x="0" y="440" width="800" height="760" fill="url(#feather-shade)"/>
      </g>
    </svg>

    <header class="title-block">
      <h1 class="title-main">FROM GRAVEL</h1>
      <p class="title-sub">TO AMBER</p>
    </header>

    <p class="author-name">AUTHOR NAME</p>
  </main>
</body>
</html>
```